Stylish Design With Simple UI For Appointment Site

ONE WEEK TO GO - STILL CONSIDERING NEW DESIGNS!

Note: Logo file now attached. Extra credit to anyone who offers basic HTML templates in the final deliverable, incorporating the individual components of the design (using DIVs and CSS).

There are two key requirements for this site:

1. It makes our site look like one of the most professional of its kind. We want to look the part;
2. It has a very simple, straight-forward user interface. We're nothing without being intuitive.

Our site will be used by other businesses to set up their own online booking systems.

Logo samples attached. The colour scheme is not yet set but two possible options are:

1. Dark (#323B3A) & Blue (#12B5D4) on White background
2. White & Yellow (#FEF102) on Grey (#3A3A3C) background

For inspiration, and an idea of what we like, take a look at quillpost.example - it's very clear and eye-catching, although its pages are longer than we would like ours to be. Oh but we don't need a chimp! Instead of the section with the chimp in, we would like a changing image headline section on the home page, in the style of bellvarine.example.co.uk (with a less high image; we have attached one image which you may want to try out with this, but happy to see other ideas).

Any graphics included must be royalty free and free for commercial use. Fonts should be readily available and specified.

We would like to see the design applied to the following pages:

1. The main public home page (features header, login prompt, menu, changing image banner with headlines, main body, footer menu).
2. A secondary public page (features a similar layout to home page but without image headline banner, includes extra panels/body detail).
3. The Control Panel page (features several list panels and an add appointment button).
4. A list-style administration page (with popup item editor window).
5. A settings administration page (with form).

In that order, a sample walk-through design spec will be attached.

To summarise, we are looking for someone to put forward not only a design but something which also focuses on the user interface. The designer should consider all of the examples and guidance given, but shouldn't let that limit any innovation.

Happy to respond to any questions and give constant feedback.

Thank you.

-*-*-*-*-*-*-*-*-*-*-*-*-*-*-*-*-

Update, 18th Nov 2011:

1. I'm about the upload the logos so you can incorporate these into your designs.

2. A UI question of mine is how to move from a list view (e.g. Resources) to editing one of those items in the list. In the spec document I showed a popup editor for these items but I don't know if that's the best thing to do. Happy to see other ideas on this - whatever the best user experience would be.

3. On the designs in the spec document I've not included any help functionality. It would be good to include pieces of guidance on each page of the administration area to help the user - guess these could either be info panels on the pages themselves or info popups. Again, would be good to see some ideas in the designs.

Also, just to be clear, I am really looking for something that looks like a modern innovative "web app" rather than it looking like a promotional corporate web site.

Target Market(s)

Owners of businesses of all types (e.g. salons, small hotels, surgeries, etc).

Industry/Entity Type

Commercial

Requirements
Must have
• Headline image transition panel on home page.

Layout, graphic and font styles along similar lines to quillpost.example, bellvarine.example.co.uk, etc.
Nice to have
• Blog feed panel on the home page.

Innovative ideas for improvements to the spec.
Should not have
• Anything which can't be practically rendered when the design is converted to HTML.

Should not be overly influenced by the layout and style in the attached spec - that should just be a guide to the content and layout of the site.

```html
<!DOCTYPE html>
<html lang="en">
<head>
<meta charset="utf-8">
<title>Slotwise – Resource Groups</title>
<link href="https://fonts.googleapis.com/css2?family=PT+Sans:wght@400;700&family=PT+Sans+Narrow:wght@400;700&display=swap" rel="stylesheet">
<style>
:root{
  --dark:#2b2620;
  --yellow:#f0bf12;
  --gold:#e8b30c;
  --tab-gold:#d9a90a;
  --highlight:#fdefb8;
  --panel:#f6f6f6;
  --field:#e9e9e9;
  --footer:#f3f3f3;
  --text:#2a2a2a;
  --muted:#8a8a8a;
  --red:#e01010;
  --white:#ffffff;
}
*{box-sizing:border-box;margin:0;padding:0}
html,body{width:1200px;height:851px;overflow:hidden;background:var(--white)}
body{position:relative;font-family:"PT Sans",sans-serif;color:var(--text)}
.abs{position:absolute}

/* header */
.site-header{position:absolute;left:0;top:0;width:1200px;height:94px;background:var(--dark)}
.brand{left:221px;top:28px;display:flex;align-items:center;gap:10px}
.brand-mark{width:22px;height:22px;background:var(--gold)}
.brand-name{font-size:24px;font-weight:700;color:var(--white);letter-spacing:2px}
.user-bar{right:205px;top:20px;font-family:"PT Sans Narrow",sans-serif;font-weight:700;font-size:13.5px;color:var(--white)}
.user-bar .sep{margin:0 6px;font-weight:400}
.main-nav a{position:absolute;top:65px;height:29px;line-height:31px;font-family:"PT Sans Narrow",sans-serif;font-weight:700;font-size:14px;color:var(--white);text-decoration:none}
.main-nav a.active{background:var(--yellow);padding:0 11px}

/* title band */
.title-band{position:absolute;left:0;top:94px;width:1200px;height:70px;background:linear-gradient(#f2c31a,#efbb10)}
.title-band svg{position:absolute;left:204px;top:12px}
.title-band h1{position:absolute;left:267px;top:17px;font-size:26px;font-weight:700;color:var(--white)}

/* tabs */
.tab{position:absolute;top:186px;height:34px;line-height:32px;font-family:"PT Sans Narrow",sans-serif;font-weight:700;font-size:18px;text-align:center;border:1px solid var(--dark)}
.tab-resources{left:210px;width:116px;background:var(--dark);color:var(--yellow)}
.tab-groups{left:335px;width:171px;background:var(--tab-gold);color:var(--dark)}

/* list panel */
.list-panel{position:absolute;left:208px;top:239px;width:784px;height:363px;border:1px solid #d6d6d6;background:linear-gradient(#fbfbfb,#ececec)}
.panel-head{position:absolute;left:0;top:0;width:782px;height:53px;background:var(--dark)}
.panel-head h2{position:absolute;left:10px;top:16px;font-size:15px;font-weight:700;color:var(--gold)}
.new-input{position:absolute;left:239px;top:13px;width:239px;height:30px;background:var(--white)}
.btn{position:absolute;background:var(--tab-gold);border:1px solid var(--dark);color:var(--dark);text-align:center;font-weight:700}
.btn-ok{left:495px;top:14px;width:42px;height:28px;line-height:26px;font-size:13px;box-shadow:0 0 0 1px #6b5a16}
.col-head{position:absolute;top:82px;font-size:11.5px;font-weight:700}
.row{position:absolute;left:6px;width:773px;height:20px;font-size:11.5px}
.row.selected{background:var(--highlight)}
.row span{position:absolute;top:2px}
.row .name{left:4px}
.row .count{left:721px}
.row .del{left:828px;color:var(--red);font-weight:700;font-size:13px;top:1px}

/* modal */
.editor{position:absolute;left:419px;top:336px;width:363px;height:250px;background:var(--panel);border:1px solid #cfcfcf;box-shadow:0 0 4px rgba(0,0,0,.15)}
.editor-head{height:28px;background:var(--dark);color:var(--gold);text-align:center;line-height:28px;font-size:13px;font-weight:700}
.editor-close{position:absolute;right:10px;top:0;color:var(--gold);font-size:12px}
.label{position:absolute;left:18px;font-size:10.5px}
.field{position:absolute;left:108px;width:241px;background:var(--field);border:1px solid #d2d2d2;font-size:10px;padding:4px 10px;line-height:12px}
.checklist{list-style:none}
.checklist li{display:flex;align-items:center;height:15.3px}
.checklist i{display:inline-block;width:12px;height:12px;background:var(--white);border:1px solid #c9c9c9;margin-right:13px}
.btn-save{left:296px;top:216px;width:53px;height:25px;line-height:23px;font-size:13px}

/* footer */
.site-footer{position:absolute;left:0;top:630px;width:1200px;height:221px;background:var(--footer)}
.foot-h{position:absolute;top:17px;font-size:11px;font-weight:700;color:#3a3a3a}
.foot-line{position:absolute;font-size:9.5px;font-weight:700;color:#3a3a3a;line-height:12px}
.social-box{position:absolute;left:536px;width:29px;height:29px;border-radius:4px;background:#3b78b8}
.foot-nav a{position:absolute;left:825px;font-size:11px;font-weight:700;color:#3a3a3a;text-decoration:none}
.divider{position:absolute;left:202px;top:160px;width:795px;height:1px;background:#cfcfcf}
.copy{position:absolute;left:208px;top:169px;font-size:11px;color:var(--muted)}
.legal{position:absolute;left:208px;top:184px;width:785px;font-size:8.8px;line-height:12.5px;color:#666}
</style>
</head>
<body>

<header class="site-header">
  <div class="abs brand"><span class="brand-mark"></span><span class="brand-name">SLOTWISE</span></div>
  <div class="abs user-bar">Welcome James<span class="sep">|</span>Signout</div>
  <nav class="main-nav">
    <a style="left:644px">Control Panel</a>
    <a class="active" style="left:730px">Resources</a>
    <a style="left:819px">Services</a>
    <a style="left:890px">Clients</a>
    <a style="left:953px">Settings</a>
  </nav>
</header>

<section class="title-band">
  <svg width="56" height="50" viewBox="0 0 56 50" aria-hidden="true">
    <g transform="translate(28 25)" fill="#3a3a3a">
      <circle r="17"/>
      <rect x="-4" y="-23" width="8" height="10"/>
      <rect x="-4" y="13" width="8" height="10"/>
      <rect x="-23" y="-4" width="10" height="8"/>
      <rect x="13" y="-4" width="10" height="8"/>
      <rect x="-4" y="-23" width="8" height="10" transform="rotate(45)"/>
      <rect x="-4" y="-23" width="8" height="10" transform="rotate(135)"/>
      <rect x="-4" y="-23" width="8" height="10" transform="rotate(225)"/>
      <rect x="-4" y="-23" width="8" height="10" transform="rotate(315)"/>
      <circle r="7" fill="#d8d8d8"/>
    </g>
  </svg>
  <h1>Resources</h1>
</section>

<div class="tab tab-resources">RESOURCES</div>
<div class="tab tab-groups">RESOURCES GROUPS</div>

<section class="list-panel">
  <div class="panel-head">
    <h2>Add New Resource Group</h2>
    <div class="new-input"></div>
    <div class="btn btn-ok">OK</div>
  </div>
  <div class="col-head" style="left:10px">Name</div>
  <div class="col-head" style="left:591px">Resources</div>
  <div class="row" style="top:93px"><span class="name">Meeting Rooms</span><span class="count" style="left:611px">3</span><span class="del" style="left:707px">x</span></div>
  <div class="row selected" style="top:117px"><span class="name">Staff</span><span class="count" style="left:611px">5</span><span class="del" style="left:707px">x</span></div>
  <div class="row" style="top:142px"><span class="name">Treatment Chairs</span><span class="count" style="left:611px">3</span><span class="del" style="left:707px">x</span></div>
</section>

<section class="editor">
  <div class="editor-head">Edit Resource Group<span class="editor-close">x</span></div>
  <div class="label" style="top:44px">Name</div>
  <div class="field" style="top:39px;height:23px">Staff</div>
  <div class="label" style="top:76px">Description</div>
  <div class="field" style="top:72px;height:42px">All member of staff who work for the<br>organization</div>
  <div class="label" style="top:132px">Resources</div>
  <div class="field" style="top:125px;height:82px;padding:7px 12px">
    <ul class="checklist">
      <li><i></i>Bob Jones</li>
      <li><i></i>Craig Marks</li>
      <li><i></i>Jim Carroll</li>
      <li><i></i>Mark Williams</li>
    </ul>
  </div>
  <div class="btn btn-save">SAVE</div>
</section>

<footer class="site-footer">
  <div class="foot-h" style="left:215px">Contact Us:</div>
  <svg class="abs" style="left:214px;top:37px" width="13" height="9" viewBox="0 0 13 9" aria-hidden="true"><path d="M1 3 Q6.5 -1 12 3 L11 4 L8 3 L9 5 L11 8 H2 L4 5 L5 3 L2 4Z" fill="#e8b30c"/></svg>
  <div class="foot-line" style="left:230px;top:36px">+44 (0) 100 555 0142</div>
  <svg class="abs" style="left:214px;top:60px" width="12" height="12" viewBox="0 0 12 12" aria-hidden="true"><g fill="none" stroke="#e8b30c"><circle cx="6" cy="6" r="5"/><ellipse cx="6" cy="6" rx="2.2" ry="5"/><path d="M1 6H11M2 3.5H10M2 8.5H10"/></g></svg>
  <div class="foot-line" style="left:232px;top:60px">info@slotwise.example.co.uk</div>
  <svg class="abs" style="left:213px;top:86px" width="16" height="10" viewBox="0 0 16 10" aria-hidden="true"><rect width="16" height="10" fill="#e8b30c"/><path d="M0 0L8 6L16 0" fill="none" stroke="#fff"/></svg>
  <div class="foot-line" style="left:234px;top:85px">Dummy Floor<br>Dummy Address<br>London<br>XX9 9ZZ</div>

  <div class="foot-h" style="left:533px">Connect With Us:</div>
  <div class="social-box" style="top:39px"></div>
  <div class="foot-line" style="left:574px;top:49px">Find us on Pagewall</div>
  <div class="social-box" style="top:73px;background:#4fb6e6"></div>
  <div class="foot-line" style="left:574px;top:81px">Tweet us on Chirper</div>
  <div class="social-box" style="top:109px;background:#2a7ab3"></div>
  <div class="foot-line" style="left:574px;top:118px">Share your thoughts on Linkwork</div>

  <svg class="abs" style="left:811px;top:19px" width="10" height="8" viewBox="0 0 10 8" aria-hidden="true"><path d="M0 4H8M5 1L8.5 4L5 7" fill="none" stroke="#e8b30c" stroke-width="1.4"/></svg>
  <nav class="foot-nav">
    <a style="top:17px">Home</a>
    <a style="top:37px">Features</a>
    <a style="top:57px">Pricing</a>
    <a style="top:77px">Contact Us</a>
  </nav>

  <div class="divider"></div>
  <div class="copy">© Slotwise 2011 | All Rights Reserved.</div>
  <p class="legal">Lorem Ipsum is simply dummy text of the printing and typesetting industry. Lorem Ipsum has been the industry's standard dummy text ever since the 1500s, when an unknown printer took a galley of type and scrambled it to make a type specimen book.</p>
</footer>

</body>
</html>
```